Letterhead & logo design project

We need a letterhead for a new company called Dornavelle Ltd a firm of Chartered Accountants and Chartered Tax Advisers based in Wrexley, Hollanshire
Updates
Please include the following:
Chartered Accountants and Chartered Tax Advisers
Industry/Entity Type
It Company
Requirements
Must have
- Must have director's name at the bottom of the letterhead. Must also contain some wording at the bottom of the page to be provided by the BQRPT at a later date

```html
<!DOCTYPE html>
<html lang="en">
<head>
<meta charset="utf-8">
<title>Dornavelle Ltd — Letterhead</title>
<link rel="stylesheet" href="https://fonts.googleapis.com/css2?family=Merienda:wght@700&family=Poiret+One&family=Didact+Gothic&display=swap">
<style>
  :root {
    --brand-blue: #1174bd;
    --rule-blue: #8fb7dc;
    --ink: #111111;
    --muted: #7a7a7a;
    --paper: #ffffff;
    --backdrop: #eef0f2;
  }
  * { margin: 0; padding: 0; box-sizing: border-box; }
  html, body {
    width: 1200px;
    height: 900px;
    overflow: hidden;
    background: var(--backdrop);
  }
  .letterhead {
    position: absolute;
    left: 300px;
    top: 26px;
    width: 600px;
    height: 848px;
    background: var(--paper);
    box-shadow: 0 2px 10px rgba(0, 0, 0, 0.08);
    overflow: hidden;
  }
  .letterhead__art {
    position: absolute;
    inset: 0;
    width: 600px;
    height: 848px;
  }
  .credentials {
    position: absolute;
    left: 42px;
    top: 30px;
    display: flex;
    align-items: flex-start;
    gap: 8px;
    font-family: "Merienda", cursive;
    font-weight: 700;
    font-size: 11.5px;
    line-height: 15px;
    color: var(--brand-blue);
  }
  .credentials__dot,
  .firm__dot {
    width: 10px;
    height: 10px;
    border-radius: 50%;
    background: var(--brand-blue);
    flex: none;
  }
  .credentials__dot { margin-top: 7px; }
  .firm {
    position: absolute;
    right: 22px;
    top: 24px;
    text-align: right;
  }
  .firm__name {
    display: flex;
    align-items: center;
    justify-content: flex-end;
    gap: 6px;
    font-family: "Poiret One", sans-serif;
    font-size: 19px;
    line-height: 22px;
    color: var(--brand-blue);
    letter-spacing: 0.2px;
  }
  .firm__dot { width: 8px; height: 8px; }
  .firm__location {
    font-family: "Poiret One", sans-serif;
    font-size: 9.5px;
    line-height: 13px;
    color: var(--muted);
    text-transform: uppercase;
    letter-spacing: 0.3px;
    margin-top: 2px;
  }
  .signatory {
    position: absolute;
    left: 262px;
    top: 750px;
    font-family: "Didact Gothic", sans-serif;
    font-size: 12px;
    color: var(--ink);
    transform: rotate(-5.5deg);
    transform-origin: left bottom;
    white-space: nowrap;
  }
  .signatory__role { font-size: 8px; }
  .tagline {
    position: absolute;
    left: 262px;
    top: 792px;
    font-family: "Didact Gothic", sans-serif;
    font-size: 11px;
    color: rgba(255, 255, 255, 0.85);
    transform: rotate(-5.5deg);
    transform-origin: left bottom;
    white-space: nowrap;
  }
</style>
</head>
<body>
  <main class="letterhead">
    <svg class="letterhead__art" viewBox="0 0 600 848" aria-hidden="true">
      <line class="header-rule" x1="20" y1="90" x2="600" y2="90" stroke="var(--rule-blue)" stroke-width="1.2"/>
      <line class="footer-rule" x1="0" y1="796" x2="600" y2="738" stroke="var(--rule-blue)" stroke-width="1.2"/>
      <path class="footer-band" d="M0 806 L600 748 L600 848 L0 848 Z" fill="var(--brand-blue)"/>
    </svg>

    <header>
      <div class="credentials">
        <span class="credentials__dot"></span>
        <p>Chartered Accountants and<br>Chartered Tax Advisers</p>
      </div>
      <div class="firm">
        <p class="firm__name"><span class="firm__dot"></span>DORNAVELLE Ltd.</p>
        <p class="firm__location">Wrexley<br>Hollanshire</p>
      </div>
    </header>

    <footer>
      <p class="signatory">Your Name, <span class="signatory__role">Director</span></p>
      <p class="tagline">some tagline text here</p>
    </footer>
  </main>
</body>
</html>
```